依頼詳細
◆依頼するLP制作の概要
・ワイヤーフレームはこちらで製作済みの為、それをもとにページのデザインの製作をお願いいたします。
※添付ファイルにてご確認ください。
・依頼するLPは1ページです。
・メインビューの画像の製作をお願いいたします。
※詳細はワイヤーにてご確認ください
・LP内で使用する素材はこちらで用意いたします。
※添付にてご確認ください。
・レスポンシブデザインでお願いします。

◆使用目的
・広告のリンク先としてLPを使用する為、LPを訪れたお客様が
弊社のドライヘッドスパを理解し施術を受けたいと思って
いただくことが目的となります。

◆備考

LPサイトのデザインをご提案いただき依頼者を決定させていただきますので
何卒よろしくお願いいたします。
ご質問等ございましたら遠慮なくご連絡ください。
サイトURL
https://kolune.jp/
ページ数
1ページ
希望イメージ
シンプル 複雑
単色 カラフル
暗い 明るい
日常 高級
遊び心 厳粛
未来的 伝統的
女性的 男性的
希望する色
黄・オレンジ系
すでに沢山のご提案をいただいており、選定に早めに取り掛かるため、
一週間提案の締め切りを前倒しさせていただきますので
ご了承いただけますと幸いでございます。

こちらの要望に最も近く、見やすさとデザイン性が気に入った為、
選ばせていただきました。

この度は弊社の募集にご提案いただきまして誠にありがとうございます。
今後とも機会がございましたら、ご応募いただけますと幸いでございます。

```html
<!DOCTYPE html>
<html lang="ja">
<head>
<meta charset="utf-8">
<title>kolune ドライヘッドスパ</title>
<link href="https://fonts.googleapis.com/css2?family=Noto+Sans+JP:wght@400;500;700&family=Noto+Serif+JP:wght@400;500;700&display=swap" rel="stylesheet">
<style>
:root{
  --orange:#f0831e;
  --orange-deep:#e46f0c;
  --orange-soft:#f6b77a;
  --peach:#fde9d6;
  --cream:#fff8f1;
  --ink:#4a4038;
  --muted:#7d7168;
  --line:#e9ddd2;
  --white:#ffffff;
}
*{margin:0;padding:0;box-sizing:border-box}
html,body{width:1200px;height:3456px;overflow:hidden;background:var(--white)}
body{font-family:"Noto Sans JP",sans-serif;color:var(--ink);position:relative}
.serif{font-family:"Noto Serif JP",serif}
.abs{position:absolute}

/* header */
.logo{left:36px;top:14px;font-size:54px;font-weight:500;color:var(--orange);letter-spacing:1px;line-height:1.2}

/* hero */
.hero{left:0;top:90px;width:1200px;height:420px;overflow:hidden}
.hero-photo{left:0;top:0;width:1200px;height:420px;
  background:
    radial-gradient(ellipse 260px 300px at 1010px 170px,#c9a48c 0%,rgba(201,164,140,.55) 45%,rgba(201,164,140,0) 75%),
    radial-gradient(ellipse 360px 260px at 820px 250px,#ead6c6 0%,rgba(234,214,198,0) 70%),
    radial-gradient(ellipse 420px 300px at 330px 140px,#d9d3cf 0%,rgba(217,211,207,0) 70%),
    linear-gradient(90deg,#f2eeeb 0%,#e4dcd6 40%,#efe6de 70%,#e8d9cc 100%)}
.hero-fade{left:0;top:0;width:1200px;height:420px;background:linear-gradient(90deg,rgba(255,255,255,.55) 0%,rgba(255,255,255,0) 40%)}
.hero-band{left:0;top:0}
.campaign{left:560px;top:80px;width:600px;height:130px;display:flex;align-items:center;gap:26px}
.campaign-date{width:96px;height:96px;border:2px solid var(--orange);color:var(--orange);display:flex;flex-direction:column;align-items:center;justify-content:center;font-size:28px;line-height:1.1;background:rgba(255,255,255,.9)}
.campaign-date small{font-size:15px;margin-top:4px}
.campaign-copy{color:var(--orange);font-size:44px;line-height:1.35;font-weight:500;text-shadow:0 0 18px rgba(255,255,255,.9)}

/* section heading */
.heading{left:0;width:1200px;text-align:center;font-size:30px;font-weight:500;color:var(--ink)}
.heading::before{content:"";display:inline-block;width:34px;height:34px;background:var(--orange);margin-right:16px;vertical-align:-6px;box-shadow:10px -10px 0 -4px var(--orange-soft)}
.heading-rule{left:360px;width:480px;height:1px;background:var(--line)}

/* about */
.about-bg{left:0;top:650px;width:1200px;height:330px;background:linear-gradient(90deg,var(--white) 0%,var(--cream) 30%,var(--cream) 70%,var(--white) 100%)}
.price-label{left:292px;top:622px;color:var(--orange);font-size:22px;line-height:1.3}
.price-list{left:230px;top:700px;width:200px}
.price-row{display:flex;align-items:center;height:72px;margin-bottom:20px;box-shadow:0 4px 10px rgba(240,131,30,.12)}
.price-min{width:70px;height:72px;background:var(--orange);color:var(--white);display:flex;flex-direction:column;align-items:center;justify-content:center;font-size:30px;line-height:1}
.price-min small{font-size:14px}
.price-yen{flex:1;height:72px;background:var(--peach);color:var(--orange);display:flex;align-items:center;padding-left:16px;font-size:26px}
.about-frame{left:618px;top:672px;width:480px;height:225px;border:2px solid var(--orange-soft)}
.about-photo{left:600px;top:655px;width:480px;height:225px;box-shadow:0 8px 22px rgba(120,80,50,.15);
  background:
    radial-gradient(ellipse 150px 110px at 300px 120px,#d8b9a4 0%,rgba(216,185,164,0) 75%),
    radial-gradient(ellipse 180px 140px at 120px 90px,#bfa999 0%,rgba(191,169,153,0) 70%),
    linear-gradient(120deg,#efe7e0,#dccdc1 55%,#f4eee9)}
.about-title{left:650px;top:905px;font-size:20px;color:var(--ink)}
.about-text{left:650px;top:940px;width:430px;font-size:12px;line-height:1.9;color:var(--muted)}

/* gallery */
.gallery{left:120px;top:1170px;width:960px;height:440px}
.g-photo{box-shadow:0 10px 24px rgba(110,80,55,.18);
  background:
    radial-gradient(ellipse 70px 90px at 50% 28%,rgba(255,236,205,.95) 0%,rgba(255,236,205,0) 80%),
    linear-gradient(180deg,#efe7df 0%,#dccbbd 55%,#b9a090 100%)}
.sq{background:var(--orange)}
.sq-line{border:2px solid var(--orange)}
.sq-soft{background:var(--orange-soft)}
.gallery-text{left:190px;top:1700px;width:820px;font-size:12px;line-height:1.9;color:var(--muted)}

/* buttons */
.btns{left:0;width:1200px;display:flex;justify-content:center;gap:24px}
.btn{width:150px;height:60px;background:var(--orange);color:var(--white);display:flex;align-items:center;justify-content:center;gap:10px;font-size:16px;font-weight:500;border-radius:2px;box-shadow:0 4px 0 var(--orange-deep)}

/* effects */
.effect-img{border:1px solid var(--line);box-shadow:10px 10px 0 var(--peach);
  background:
    radial-gradient(ellipse 60px 70px at 50% 40%,#f5cfa8 0%,rgba(245,207,168,0) 80%),
    linear-gradient(135deg,#fffaf4,#f7e8d8)}
.effect-title{font-size:20px;color:var(--ink);display:flex;align-items:center;gap:10px}
.effect-num{width:30px;height:30px;background:var(--orange);color:var(--white);font-size:16px;display:flex;align-items:center;justify-content:center}
.effect-text{font-size:12px;line-height:1.9;color:var(--muted);margin-top:12px}

/* access */
.access-title{left:0;top:2690px;width:1200px;text-align:center;font-size:30px;color:var(--ink)}
.map{left:370px;top:2755px;width:460px;height:205px;border:1px solid var(--line);
  background:
    linear-gradient(28deg,transparent 48%,#ffffff 48%,#ffffff 51%,transparent 51%),
    linear-gradient(115deg,transparent 60%,#f7d9b4 60%,#f7d9b4 63%,transparent 63%),
    linear-gradient(135deg,#eef0ec,#e1e6e0 50%,#f1efe9)}
.shop-photo{left:370px;top:2985px;width:210px;height:205px;box-shadow:0 8px 20px rgba(110,80,55,.16);
  background:
    radial-gradient(ellipse 50px 60px at 50% 35%,rgba(255,236,205,.9) 0%,rgba(255,236,205,0) 80%),
    linear-gradient(160deg,#e9dfd4,#c9b6a6)}
.shop-info{left:604px;top:2995px;width:300px;font-size:12px;line-height:1.95;color:var(--ink)}
.shop-info .name{font-size:14px;font-weight:500}

footer{position:absolute;left:0;top:3414px;width:1200px;height:42px;background:var(--orange);color:var(--white);font-size:12px;display:flex;align-items:center;justify-content:center;letter-spacing:1px}
</style>
</head>
<body>

<header>
  <div class="abs logo">kolune</div>
</header>

<section class="abs hero">
  <div class="abs hero-photo" role="img" aria-label="ヘッドスパ施術を受ける女性と施術者の写真"></div>
  <div class="abs hero-fade"></div>
  <svg class="abs hero-band" width="1200" height="420" viewBox="0 0 1200 420">
    <polygon points="0,300 1200,150 1200,185 0,340" fill="#f6b77a" opacity=".75"/>
    <polygon points="0,345 1200,190 1200,260 0,420" fill="#f0831e"/>
    <polygon points="0,420 1200,260 1200,420" fill="#ffffff"/>
  </svg>
  <div class="abs campaign">
    <div class="campaign-date serif">1/31<small>まで</small></div>
    <div class="campaign-copy serif">キャンペーン価格<br>40 分 2,900 円</div>
  </div>
</section>

<h2 class="abs heading serif" style="top:566px">kolune ドライヘッドスパについて</h2>
<div class="abs heading-rule" style="top:612px"></div>

<div class="abs about-bg"></div>
<div class="abs price-label serif">料金<br>price</div>
<div class="abs price-list">
  <div class="price-row"><div class="price-min serif">25<small>min</small></div><div class="price-yen serif">¥2,900</div></div>
  <div class="price-row"><div class="price-min serif">40<small>min</small></div><div class="price-yen serif">¥4,400</div></div>
  <div class="price-row"><div class="price-min serif">55<small>min</small></div><div class="price-yen serif">¥5,900</div></div>
</div>
<div class="abs about-frame"></div>
<div class="abs about-photo" role="img" aria-label="ヘッドスパでくつろぐ女性の写真"></div>
<div class="abs about-title serif">心地よい、特別を</div>
<p class="abs about-text">頭皮と首筋を丁寧にほぐし、日々の疲れをやさしく解きほぐします。濡らさずに行うため、お仕事帰りやお出かけ前にも気軽にお立ち寄りいただけます。<br>プライベートな空間で、自分だけの穏やかな時間をお過ごしください。</p>

<h2 class="abs heading serif" style="top:1058px">オトナ女子向け、お洒落空間</h2>
<div class="abs heading-rule" style="top:1104px"></div>

<div class="abs gallery">
  <div class="abs sq" style="left:-10px;top:20px;width:70px;height:70px"></div>
  <div class="abs sq-line" style="left:20px;top:0;width:90px;height:90px"></div>
  <div class="abs g-photo" role="img" aria-label="店内の受付スペースの写真" style="left:40px;top:60px;width:200px;height:330px"></div>
  <div class="abs g-photo" role="img" aria-label="施術用チェアが並ぶ店内の写真" style="left:270px;top:30px;width:200px;height:330px"></div>
  <div class="abs sq-soft" style="left:440px;top:350px;width:60px;height:60px"></div>
  <div class="abs g-photo" role="img" aria-label="落ち着いた照明の施術ブースの写真" style="left:500px;top:70px;width:200px;height:330px"></div>
  <div class="abs g-photo" role="img" aria-label="丸い鏡のあるパウダースペースの写真" style="left:730px;top:30px;width:200px;height:330px"></div>
  <div class="abs sq" style="left:880px;top:-10px;width:60px;height:60px"></div>
  <div class="abs sq-line" style="left:860px;top:330px;width:100px;height:100px"></div>
  <div class="abs sq" style="left:900px;top:380px;width:60px;height:60px"></div>
</div>
<p class="abs gallery-text">白を基調にした落ち着きのある空間をご用意しております。<br>施術後はそのままお出かけいただけるよう、パウダースペースも完備。女性おひとりでも安心してお過ごしいただけます。</p>

<div class="abs btns" style="top:1785px">
  <div class="btn"><svg width="18" height="18" viewBox="0 0 24 24" fill="none" stroke="#fff" stroke-width="2"><rect x="3" y="4" width="18" height="17" rx="2"/><path d="M3 9h18M8 2v4M16 2v4"/></svg>WEBで予約</div>
  <div class="btn"><svg width="18" height="18" viewBox="0 0 24 24" fill="none" stroke="#fff" stroke-width="2"><rect x="6" y="2" width="12" height="20" rx="2"/><path d="M11 18h2"/></svg>電話で予約</div>
</div>

<h2 class="abs heading serif" style="top:1902px">ドライヘッドスパの効果</h2>
<div class="abs heading-rule" style="top:1948px"></div>

<div class="abs effect-img" role="img" aria-label="目の疲れを感じる女性のイラスト" style="left:330px;top:2010px;width:200px;height:200px"></div>
<div class="abs" style="left:560px;top:2030px;width:320px">
  <div class="effect-title serif"><span class="effect-num">01</span>眼精疲労の改善</div>
  <p class="effect-text">目の周りから頭部へつながる筋肉をほぐし、パソコンやスマートフォンで酷使した目の疲れをやわらげます。</p>
</div>

<div class="abs" style="left:320px;top:2240px;width:320px">
  <div class="effect-title serif"><span class="effect-num">02</span>リラックス、睡眠の質の向上</div>
  <p class="effect-text">ゆったりとした手技で心身の緊張をほどき、深いリラックスへと導きます。眠りが浅い方にもおすすめです。</p>
</div>
<div class="abs effect-img" role="img" aria-label="穏やかに眠る女性のイラスト" style="left:670px;top:2230px;width:210px;height:200px"></div>

<div class="abs effect-img" role="img" aria-label="頭を抱えて悩む女性のイラスト" style="left:330px;top:2450px;width:200px;height:200px"></div>
<div class="abs" style="left:560px;top:2470px;width:320px">
  <div class="effect-title serif"><span class="effect-num">03</span>自律神経の調整</div>
  <p class="effect-text">頭部の緊張をゆるめることで、乱れがちな自律神経のバランスを整え、心地よい毎日をサポートします。</p>
</div>

<h2 class="abs access-title serif">Access</h2>
<div class="abs map" role="img" aria-label="店舗周辺の地図"></div>
<div class="abs shop-photo" role="img" aria-label="店舗内観の写真"></div>
<div class="abs shop-info">
  <div class="name">ドライヘッドスパ kolune</div>
  東京都港区みどり町4-5-6<br>
  TEL：03-0000-4821<br>
  営業時間　平日 10:00〜22:00<br>
  土日祝 10:00〜20:00<br>
  駅より徒歩3分<br>
  ［予約制です］
</div>

<div class="abs btns" style="top:3270px">
  <div class="btn"><svg width="18" height="18" viewBox="0 0 24 24" fill="none" stroke="#fff" stroke-width="2"><rect x="3" y="4" width="18" height="17" rx="2"/><path d="M3 9h18M8 2v4M16 2v4"/></svg>WEBで予約</div>
  <div class="btn"><svg width="18" height="18" viewBox="0 0 24 24" fill="none" stroke="#fff" stroke-width="2"><rect x="6" y="2" width="12" height="20" rx="2"/><path d="M11 18h2"/></svg>電話で予約</div>
</div>

<footer>© Copyright kolune All rights reserved.</footer>
</body>
</html>
```